Marlowe Holdings LLC - Business Cards

Need the following information on the cards:

Name: Dean R Vossler
Title: Chief Executive Manager

Business address:
412 N Ridgeview Lane #118
Ashford Park, Il 60412

Phone: (630) 555-0148 - Business
KPV FFL license number: 5-21-xxx-xx-xx-04519
Email: dean.vossler@marloweholdingsffl.com

Target Market(s)

Firearm owners

Industry/Entity Type

Firearms industry,

Contact Information for Business Card

Contact number, name and title, web page address, email, business address and kpv license number,

Requirements
Must have
• Name, title, business address, phone numbers, KPV license numbers, web page address and email address.
Nice to have
• Cellphone number,

```html
<!DOCTYPE html>
<html lang="en">
<head>
<meta charset="utf-8">
<title>Marlowe Holdings LLC – Business Cards</title>
<link rel="stylesheet" href="https://fonts.googleapis.com/css2?family=PT+Sans:ital,wght@0,400;0,700;1,400&family=PT+Sans+Narrow:wght@400;700&display=swap">
<style>
  :root {
    --brand-red: #c71014;
    --ink: #1b1b1b;
    --paper: #ffffff;
    --backdrop: #b9b9b9;
    --divider: #2a2a2a;
  }
  * { box-sizing: border-box; margin: 0; padding: 0; }
  html, body {
    width: 1200px; height: 848px; overflow: hidden;
    background: var(--backdrop);
  }
  .sheet {
    position: relative; width: 1200px; height: 848px;
    display: flex; justify-content: center; align-items: center; gap: 60px;
  }
  .card {
    width: 389px; height: 680px; border-radius: 40px;
    overflow: hidden; position: relative;
    display: flex; flex-direction: column; align-items: center;
  }
  .card--front { background: var(--brand-red); justify-content: center; }
  .card--back {
    background: var(--paper); padding: 30px 28px; color: var(--ink);
    font-family: "PT Sans Narrow", "PT Sans", sans-serif; text-align: center;
    justify-content: center;
  }
  .brand { display: flex; flex-direction: column; align-items: center; gap: 12px; }
  .brand__circle {
    width: 100px; height: 100px; border-radius: 50%;
    border: 3px solid currentColor;
  }
  .brand__name {
    font-family: "PT Sans", sans-serif; font-weight: 700;
    font-size: 24px; line-height: 1.15; letter-spacing: 2px;
    text-transform: uppercase; text-align: center;
  }
  .card--front .brand { color: var(--paper); gap: 16px; }
  .card--front .brand__circle { width: 170px; height: 170px; }
  .card--front .brand__name { font-size: 34px; }
  .card--back .brand { color: var(--brand-red); }
  .person { margin-top: 18px; }
  .person__name {
    font-family: "PT Sans", sans-serif; font-weight: 700;
    font-size: 34px; line-height: 1.1;
  }
  .person__title {
    color: var(--brand-red); font-weight: 700; font-size: 21px;
    text-transform: uppercase; letter-spacing: .3px; margin-top: 2px;
  }
  .license {
    font-family: "PT Sans", sans-serif; font-style: italic;
    font-size: 16px; line-height: 1.3; margin-top: 8px;
  }
  .divider {
    width: 230px; height: 2px; margin: 16px auto 12px;
    background: linear-gradient(90deg, transparent, var(--divider) 30%, var(--divider) 70%, transparent);
  }
  .icons { display: flex; justify-content: center; gap: 14px; margin-bottom: 6px; }
  .icons svg { width: 24px; height: 24px; fill: none; stroke: var(--brand-red); stroke-width: 2; }
  .contact { font-size: 19px; line-height: 1.32; }
</style>
</head>
<body>
<main class="sheet">
  <section class="card card--front" aria-label="Card front">
    <div class="brand">
      <span class="brand__circle"></span>
      <span class="brand__name">Marlowe<br>Holdings LLC</span>
    </div>
  </section>

  <section class="card card--back" aria-label="Card back">
    <div class="brand">
      <span class="brand__circle"></span>
      <span class="brand__name">Marlowe<br>Holdings LLC</span>
    </div>

    <div class="person">
      <h1 class="person__name">Dean R Vossler</h1>
      <p class="person__title">Chief Executive Manager</p>
    </div>
    <p class="license">KPV FFL license number:<br>5-21-xxx-xx-xx-04519</p>

    <div class="divider"></div>
    <div class="icons">
      <svg viewBox="0 0 24 24" aria-hidden="true"><path d="M6 3h4l1.5 5-2.5 1.5a11 11 0 0 0 5.5 5.5L16 12.5l5 1.5v4a2 2 0 0 1-2 2A16 16 0 0 1 4 5a2 2 0 0 1 2-2z"/></svg>
      <svg viewBox="0 0 24 24" aria-hidden="true"><rect x="6" y="2" width="12" height="20" rx="2"/><rect x="8.5" y="5" width="7" height="7"/><path d="M9 15h6M9 18h6"/></svg>
    </div>
    <p class="contact">Phone: (630) 555-0148<br>Cellphone: (630) 555-0193</p>

    <div class="divider"></div>
    <div class="icons">
      <svg viewBox="0 0 24 24" aria-hidden="true"><rect x="3" y="5" width="18" height="14"/><path d="M3 5l9 8 9-8"/></svg>
      <svg viewBox="0 0 24 24" aria-hidden="true"><circle cx="12" cy="12" r="9"/><path d="M3 12h18M12 3c-4 5-4 13 0 18M12 3c4 5 4 13 0 18"/></svg>
      <svg viewBox="0 0 24 24" aria-hidden="true"><path d="M12 22s-7-7.5-7-12a7 7 0 0 1 14 0c0 4.5-7 12-7 12z"/><circle cx="12" cy="10" r="2.5"/></svg>
    </div>
    <p class="contact">
      dean.vossler@marloweholdingsffl.com<br>
      www.marloweholdingsffl.com<br>
      412 N Ridgeview Lane #118<br>
      Ashford Park, Il 60412
    </p>
  </section>
</main>
</body>
</html>
```